Instagram background for quotes

We need a 1080x1080 background for instagram. I use the Phonto app to put text over the image.

We create motivating and inspiring messages for our followers on IG.

Our brands message is, "Mediocre thinking leads to mediocre results. Get Mission - Get Motivated - Get Moving
https://www.example-social.test/steel_resolve_co/

We would like to move away from the rustic look and have a gloss black background with the goal of using text that is cleaner to match the SR in the logo.

I see the design remaining fairly close to what it is now with the logo at the top. I like the quotes on this brand here, https://www.example-social.test/talkwithtycoons/?hl=en. I see this being built into our new background with the quotations being aggressive to match the wings in our logo.

Here is another brand we like - https://www.example-social.test/boomboomdrive/

I've attached the files I was given by the logo designer who has disappeared. I am hoping what is there will suffice.

Target Market(s)

24-34 year old males

Industry/Entity Type

Quotes

Colors
000000
ffffff

Requirements
Must have
• Provided Logo without text
Nice to have
• Aggressive looking quotes to match wings
• Watermark logo in background

```html
<!DOCTYPE html>
<html lang="en">
<head>
<meta charset="utf-8">
<title>Steel Resolve – Quote Background</title>
<link rel="stylesheet" href="https://fonts.googleapis.com/css2?family=Iceland&display=swap">
<style>
  :root {
    --bg: #000000;
    --frame: #ffffff;
    --panel-top: #2c2c2c;
    --panel-bottom: #171717;
    --panel-edge: rgba(150, 215, 215, 0.55);
    --quote: #d2d2d2;
    --quote-shade: #6a6a6a;
    --screw: #000000;
    --screw-ring: #8a8a8a;
    --watermark: rgba(255, 255, 255, 0.035);
  }
  * { margin: 0; padding: 0; box-sizing: border-box; }
  html, body { width: 1200px; height: 1200px; overflow: hidden; background: var(--bg); }
  .canvas {
    position: relative;
    width: 1200px;
    height: 1200px;
    background: var(--bg);
    font-family: "Iceland", sans-serif;
  }
  .frame-lines { position: absolute; inset: 0; }
  .glass-panel {
    position: absolute;
    left: 83px; top: 83px;
    width: 1034px; height: 1034px;
    border: 2px solid var(--panel-edge);
    border-radius: 22px;
    background:
      linear-gradient(125deg, rgba(255,255,255,0) 38%, rgba(255,255,255,0.05) 39%, rgba(255,255,255,0.05) 62%, rgba(255,255,255,0) 63%),
      linear-gradient(160deg, var(--panel-top), var(--panel-bottom));
    overflow: hidden;
  }
  .watermark-name {
    position: absolute;
    left: 0; right: 0; top: 330px;
    text-align: center;
    font-size: 420px;
    line-height: 1;
    color: var(--watermark);
  }
  .screw {
    position: absolute;
    width: 20px; height: 20px;
    border-radius: 50%;
    background: var(--screw);
    border: 2px solid var(--screw-ring);
  }
  .screw--tl { left: 137px; top: 125px; }
  .screw--tr { left: 1053px; top: 125px; }
  .screw--bl { left: 119px; top: 1063px; }
  .screw--br { left: 1053px; top: 1063px; }
  .brand-badge {
    position: absolute;
    left: 470px; top: 10px;
    width: 260px; height: 150px;
    display: flex; align-items: center; justify-content: center; gap: 14px;
    color: var(--frame);
    font-size: 96px;
    line-height: 1;
  }
  .brand-badge__mark {
    width: 26px; height: 26px;
    border: 3px solid var(--frame);
  }
  .quote {
    position: absolute;
    left: 0; right: 0;
    text-align: center;
    color: var(--quote);
    font-size: 84px;
    line-height: 88px;
    letter-spacing: 3px;
    text-shadow: 0 2px 0 var(--quote-shade), 0 -1px 0 #f4f4f4;
  }
  .quote--message { top: 312px; }
  .quote--mantra { top: 660px; line-height: 85px; }
  .profile-link {
    position: absolute;
    left: 0; right: 0; top: 1142px;
    text-align: center;
    color: var(--frame);
    font-size: 32px;
    letter-spacing: 1px;
    line-height: 1;
  }
</style>
</head>
<body>
<div class="canvas">
  <svg class="frame-lines" width="1200" height="1200" viewBox="0 0 1200 1200" aria-hidden="true">
    <g fill="none" stroke="var(--frame)" stroke-width="3">
      <polyline points="445,47 47,47 47,1153 262,1153"/>
      <polyline points="755,47 1153,47 1153,1153 938,1153"/>
    </g>
  </svg>

  <div class="glass-panel">
    <div class="watermark-name">SR</div>
  </div>

  <span class="screw screw--tl"></span>
  <span class="screw screw--tr"></span>
  <span class="screw screw--bl"></span>
  <span class="screw screw--br"></span>

  <div class="brand-badge">
    <span class="brand-badge__mark"></span>
    <span class="brand-badge__name">SR</span>
  </div>

  <p class="quote quote--message">Mediocre thinking<br>leads to<br>mediocre results.</p>
  <p class="quote quote--mantra">- Get Mission -<br>- Get Motivated -<br>- Get Moving -</p>

  <p class="profile-link">https://www.example-social.test/steel_resolve_co/</p>
</div>
</body>
</html>
```